Marlow Cybersecurity Secives professional web site

Marlow is a unit of the Tesselcore company, based on the audit services it offers and which mainly works by the contacts it has from its previous experience. The objective with the development of this website will be to increase its presence on the internet and even link the traffic of its social networks with the blog of the new page and in this way, provide information for old and potential customers.
For this reason, we will set the objective of the page, have all the information of the company, its services and its scope in general, in a formal and simple for users, facilitating the task of finding the information they want within of the page, as well as, including the option of feedback.

Target Market(s)

any company that needs security assessments

Number of Pages Required

4 page

Font styles to use
Sans Serif

Colors

Designer to choose colors to be used in the design.

Requirements
Must have
• READ THE PDF PLEASE. Video in homepage, cool graphics, color like our logo
• I like the following sites: www.tesselcore-example.com & www.quarbitex-example.com
Nice to have
• Futuristic
Should not have
• Please, dont use the gallery pictures I used in my document, I prefer hand made illustrations instead

```html
<!DOCTYPE html>
<html lang="en">
<head>
<meta charset="utf-8">
<title>Marlow Security – Web Pages</title>
<link href="https://fonts.googleapis.com/css2?family=Arimo:wght@400;700&family=Montserrat:wght@700;800&display=swap" rel="stylesheet">
<style>
  :root {
    --backdrop: #b3b3b3;
    --white: #ffffff;
    --ink: #1c1c1c;
    --nav-ink: #333333;
    --navy: #1d3552;
    --navy-deep: #142840;
    --navy-glow: #27466a;
    --brand-dark: #1b2a3a;
    --panel: rgba(88, 74, 62, 0.38);
  }
  * { box-sizing: border-box; margin: 0; padding: 0; }
  html, body {
    width: 1200px; height: 1200px; overflow: hidden;
    background: var(--backdrop);
    font-family: "Arimo", Arial, sans-serif;
    color: var(--ink);
  }
  .canvas { position: relative; width: 1200px; height: 1200px; }

  .page { position: absolute; background: var(--white); overflow: hidden; }
  .page--services { left: 207px; top: 38px; width: 786px; height: 548px; }
  .page--blog { left: 213px; top: 622px; width: 774px; height: 539px; }

  .site-header { position: absolute; left: 0; top: 0; width: 100%; height: 68px; }
  .brand { position: absolute; top: 15px; display: flex; align-items: center; gap: 8px; }
  .brand__name {
    font-family: "Montserrat", Arial, sans-serif; font-weight: 800;
    font-size: 17px; line-height: 15px; color: var(--brand-dark);
    text-align: right; letter-spacing: -0.3px;
  }
  .brand__dot { width: 44px; height: 44px; border-radius: 50%; background: var(--brand-dark); }

  .nav-item {
    position: absolute; top: 38px; transform: translate(-50%, -50%);
    font-family: "Arimo", Arial, sans-serif; font-weight: 700; font-size: 10.5px;
    color: var(--nav-ink); letter-spacing: 0.2px; white-space: nowrap;
  }
  .nav-item--active::after {
    content: ""; position: absolute; left: 0; right: 0; top: 17px;
    height: 2.5px; background: #444;
  }
  .nav-item--blog-active::after { left: -11px; right: -11px; }

  .social-dot {
    position: absolute; top: 17px; width: 10px; height: 10px;
    border-radius: 50%; background: #333;
  }

  .hero {
    position: absolute; left: 0; top: 68px; width: 100%;
    background:
      radial-gradient(circle at 30% 20%, var(--navy-glow) 0%, transparent 45%),
      radial-gradient(circle at 80% 75%, #223c5c 0%, transparent 50%),
      linear-gradient(160deg, var(--navy) 0%, var(--navy-deep) 100%);
  }
  .page--services .hero { height: 412px; }
  .page--blog .hero { height: 406px; }

  .service-card {
    position: absolute; width: 214px; height: 152px;
    background: var(--white); padding: 0 10px;
  }
  .service-card__title {
    font-family: "Arimo", Arial, sans-serif; font-weight: 700;
    font-size: 9.8px; letter-spacing: 1px; text-align: center;
    margin: 14px -6px 0; line-height: 11px; white-space: nowrap;
  }
  .service-card__title--left { text-align: left; margin: 10px 0 0; }
  .service-card__body { font-size: 9.2px; line-height: 11.5px; margin-top: 9px; }
  .service-card__body--fine { font-size: 6.6px; line-height: 9px; }
  .service-card__body--fine p + p { margin-top: 9px; }
  .service-card b { font-weight: 700; }

  .blog-panel { position: absolute; left: 99px; width: 576px; height: 117px; background: var(--panel); }

  .site-footer { position: absolute; left: 0; bottom: 0; width: 100%; height: 68px; }
  .footer-link {
    position: absolute; display: flex; align-items: center; gap: 3px;
    font-size: 10.4px; letter-spacing: 0.8px; color: #333;
    transform: translateY(-50%);
  }
  .footer-link::before {
    content: ""; width: 8px; height: 8px; border-radius: 50%; background: #333;
  }
</style>
</head>
<body>
<div class="canvas">

  <section class="page page--services">
    <header class="site-header">
      <div class="brand" style="left:43px">
        <div class="brand__name">MARLOW<br>SECURITY</div>
        <div class="brand__dot"></div>
      </div>
      <span class="nav-item" style="left:253px">HOME</span>
      <span class="nav-item" style="left:345px">COMPANY</span>
      <span class="nav-item nav-item--active" style="left:447px">SERVICES</span>
      <span class="nav-item" style="left:538px">BLOG</span>
      <span class="nav-item" style="left:629px">CONTACT</span>
      <span class="social-dot" style="left:694px"></span>
      <span class="social-dot" style="left:720px"></span>
      <span class="social-dot" style="left:745px"></span>
    </header>

    <div class="hero" role="img" aria-label="Dark navy backdrop with a faint network of connected nodes">
      <article class="service-card" style="left:59px;top:48px">
        <h3 class="service-card__title">WEBPAGE AUDIT</h3>
        <p class="service-card__body" style="margin-top:6px"><b>Web page audits:</b> in this type of service we locate design and programming errors, review the web with and without the user, its structure and related technologies (authentication and authorization framework, session management). Likewise, to complement the service we carry out the review of the business logic and the interaction with the client.</p>
      </article>
      <article class="service-card" style="left:286px;top:48px">
        <h3 class="service-card__title">INTERNAL AND EXTERNAL AUDIT</h3>
        <p class="service-card__body" style="margin-top:10px;padding:0 2px"><b>External and internal audits:</b> within this service we offer the vulnerability scan in network, servers and protocol. We also perform an analysis of them, and to give a more complete service we perform controlled exploitation and lateral movement.</p>
      </article>
      <article class="service-card" style="left:513px;top:48px">
        <h3 class="service-card__title">WEB APPLICATION AUDIT</h3>
        <div class="service-card__body service-card__body--fine" style="margin-top:9px">
          <p><b>Audits of Nimbus OS and Corvid applications:</b> we include in this service the analysis of the app's communications (including remote web service), the review of the configuration files, the revision of the local databases and the analysis of the code</p>
          <p><b>Audits of IoT devices:</b> we include in this service the analysis of the communications of the device (including remote web services), the revision of the hardware and the firmware</p>
        </div>
      </article>

      <article class="service-card" style="left:59px;top:212px">
        <h3 class="service-card__title">SOURCE CODE AUDIT</h3>
        <p class="service-card__body" style="margin-top:11px;padding-left:2px"><b>Source code audit:</b> for this service we analyze and review the code identifying both the architecture, data flows and threat modeling.</p>
      </article>
      <article class="service-card" style="left:286px;top:212px">
        <h3 class="service-card__title service-card__title--left" style="padding-left:2px">DIGITAL FORENSICS<br>&amp; INCIDENT RESPONSE</h3>
        <p class="service-card__body" style="margin-top:7px"><b>Response to incidents:</b> service provided by a team of highly qualified professionals in response to incidents, with experience in containing cyber threats in corporate environments. It integrates the services of penetration testing, networks, systems administration, forensic analysis and malware reversing.</p>
      </article>
      <article class="service-card" style="left:513px;top:212px">
        <h3 class="service-card__title">REPORT RESOLUTION</h3>
        <p class="service-card__body" style="margin-top:11px"><b>Resolution of reports:</b> we offer an executive summary with all the detailed vulnerabilities, you can go to our technical team if you do not know how to solve them, they will always be at your disposal.</p>
      </article>
    </div>

    <footer class="site-footer">
      <span class="footer-link" style="left:277px;top:35px">Chirper</span>
      <span class="footer-link" style="left:361px;top:34px">Snapgrid</span>
      <span class="footer-link" style="left:461px;top:34px">Blog</span>
    </footer>
  </section>

  <section class="page page--blog">
    <header class="site-header">
      <div class="brand" style="left:42px">
        <div class="brand__name">MARLOW<br>SECURITY</div>
        <div class="brand__dot"></div>
      </div>
      <span class="nav-item" style="left:249px">HOME</span>
      <span class="nav-item" style="left:339px">COMPANY</span>
      <span class="nav-item" style="left:441px">SERVICES</span>
      <span class="nav-item nav-item--active nav-item--blog-active" style="left:531px">BLOG</span>
      <span class="nav-item" style="left:620px">CONTACT</span>
      <span class="social-dot" style="left:685px"></span>
      <span class="social-dot" style="left:709px"></span>
      <span class="social-dot" style="left:734px"></span>
    </header>

    <div class="hero" role="img" aria-label="Dark navy backdrop with a faint network of connected nodes">
      <div class="blog-panel" style="top:71px"></div>
      <div class="blog-panel" style="top:219px"></div>
    </div>

    <footer class="site-footer">
      <span class="footer-link" style="left:273px;top:38px">Chirper</span>
      <span class="footer-link" style="left:355px;top:37px">Snapgrid</span>
      <span class="footer-link" style="left:454px;top:37px">Blog</span>
    </footer>
  </section>

</div>
</body>
</html>
```